Rinaldo's Top Paw Haven 555

I'm a Veterinary Assitant over 20 year experience in West Los Angeles with wealthy clients . I just open a business which will include Petsitting in my house dogs and cats only visiting clients house's stay overnights , transporting animal to the hospital or physical therapy
Services including small % of dog walking , nail trim , ear cleaning , giving medication , Sq fluids , passive of range and motion post surgery many of my clients is all referral from veterinary's either general practice or specialist . I already got the
Ficstitious Bussines Statement going and in the process of getting a Petsitting insurance with a good cover also I will have a website with many clients testimonies and Veterinary references . Hope this is enough information . Thanks Rinaldo feel free to contact me with any questions

Target Market(s)

Pet Owners that are pet lovers but really busy not able to give medication
Or care for the pet

Industry/Entity Type

Business

Contact Information for Business Card

Bussines based on love and care for pets wellbeing driven by trust and reliability .

Font styles to use
Serif
Decorative

Colors
00a990
33b8a4
30b7a3

Requirements
Must have
• The bussines name ,
• Over 20 years experience as a Veterinay Assitant
• Pet Sitting / In Home Care / Transportation
• Licensed and Insured
• Phone 310- 647-3918
• Website : rinaldotoppawhaven555.com
• email: info@rinaldotoppawhaven555.com
Nice to have
• Please give me a idea
Should not have
• no address on the business card .

```html
<!DOCTYPE html>
<html lang="en">
<head>
<meta charset="utf-8">
<title>Rinaldo's Top Paw Haven 555 – Business Card</title>
<link href="https://fonts.googleapis.com/css2?family=Montserrat:wght@400;500;600;700&display=swap" rel="stylesheet">
<style>
  :root {
    --teal: #00a990;
    --teal-light: #33b8a4;
    --teal-soft: #30b7a3;
    --blue: #2a6db5;
    --navy: #1f2a8c;
    --card: #f4f5f6;
    --card-shade: #e6e8ea;
    --backdrop: #dcdedf;
  }
  * { box-sizing: border-box; margin: 0; padding: 0; }
  html, body { width: 1200px; height: 800px; overflow: hidden; }
  body {
    background: var(--backdrop);
    font-family: "Montserrat", sans-serif;
    display: flex; align-items: center; justify-content: center; gap: 40px;
  }
  .card {
    position: relative; width: 540px; height: 309px;
    background: linear-gradient(135deg, #ffffff 0%, var(--card) 55%, var(--card-shade) 100%);
    box-shadow: 0 10px 24px rgba(0,0,0,.18);
    overflow: hidden;
  }
  .card-bands { position: absolute; inset: 0; width: 100%; height: 100%; }
  .brand { display: flex; align-items: center; gap: 10px; position: absolute; }
  .brand-dot { width: 26px; height: 26px; border-radius: 50%; background: var(--teal); flex: none; }
  .brand-name { color: var(--blue); font-weight: 700; line-height: 1.1; text-transform: uppercase; }
  .card-front .brand { left: 50%; top: 86px; transform: translateX(-50%); }
  .card-front .brand-name { font-size: 22px; width: 250px; }
  .tagline {
    position: absolute; right: 26px; top: 222px;
    color: var(--teal); font-size: 13px; font-weight: 500;
  }
  .card-back .brand { left: 28px; top: 172px; }
  .card-back .brand-name { font-size: 15px; width: 160px; }
  .details { position: absolute; left: 232px; top: 62px; color: var(--blue); }
  .owner-name { font-size: 22px; font-weight: 700; letter-spacing: .5px; }
  .owner-name .surname { color: var(--teal-light); }
  .owner-role { font-size: 11px; color: var(--teal); letter-spacing: 1px; margin-bottom: 6px; }
  .services { font-size: 12.5px; font-weight: 600; line-height: 1.35; }
  .credentials { font-size: 12.5px; font-weight: 400; margin-bottom: 6px; }
  .contact { list-style: none; font-size: 12.5px; color: var(--teal); line-height: 1.6; }
  .contact li { display: flex; align-items: center; gap: 8px; }
  .contact svg { width: 12px; height: 12px; fill: var(--blue); flex: none; }
</style>
</head>
<body>

<section class="card card-front" aria-label="Card front">
  <svg class="card-bands" viewBox="0 0 540 309" preserveAspectRatio="none" aria-hidden="true">
    <rect x="0" y="0" width="540" height="9" fill="var(--teal-light)"/>
    <polyline points="0,250 170,250 192,236 540,236" fill="none" stroke="var(--navy)" stroke-width="2"/>
    <polygon points="0,258 170,258 192,244 540,244 540,309 0,309" fill="var(--teal-soft)"/>
  </svg>
  <div class="brand">
    <span class="brand-dot"></span>
    <span class="brand-name">Rinaldo's Top Paw Haven 555</span>
  </div>
  <p class="tagline">Honored And Privileged To Be A Part Of Your Pets Life</p>
</section>

<section class="card card-back" aria-label="Card back">
  <svg class="card-bands" viewBox="0 0 540 309" preserveAspectRatio="none" aria-hidden="true">
    <polygon points="0,0 540,0 540,26 330,26 308,40 0,40" fill="var(--teal-soft)"/>
    <polyline points="0,46 308,46 330,32 540,32" fill="none" stroke="var(--navy)" stroke-width="2"/>
    <polyline points="0,270 200,270 222,256 540,256" fill="none" stroke="var(--navy)" stroke-width="2"/>
    <polygon points="0,276 200,276 222,262 540,262 540,309 0,309" fill="var(--teal-soft)"/>
  </svg>
  <div class="brand">
    <span class="brand-dot"></span>
    <span class="brand-name">Rinaldo's Top Paw Haven 555</span>
  </div>
  <div class="details">
    <h1 class="owner-name">RINALDO <span class="surname">MORETTI</span></h1>
    <p class="owner-role">OWNER</p>
    <p class="services">Vet Assistant over 20 year of experience<br>Pet Sitting / In Home Care / Transportation</p>
    <p class="credentials">Licensed And Insured</p>
    <ul class="contact">
      <li><svg viewBox="0 0 24 24" aria-hidden="true"><path d="M6.6 10.8a15 15 0 0 0 6.6 6.6l2.2-2.2c.3-.3.7-.4 1-.2 1.1.4 2.3.6 3.6.6.6 0 1 .4 1 1V20c0 .6-.4 1-1 1A17 17 0 0 1 3 4c0-.6.4-1 1-1h3.5c.6 0 1 .4 1 1 0 1.3.2 2.5.6 3.6.1.3 0 .7-.2 1z"/></svg>(310) 647-3918</li>
      <li><svg viewBox="0 0 24 24" aria-hidden="true"><path d="M2 5h20v14H2zm2 2v.5l8 5 8-5V7zm0 2.9V17h16V9.9l-8 5z"/></svg>info@rinaldotoppawhaven555.com</li>
      <li><svg viewBox="0 0 24 24" aria-hidden="true"><path d="M12 2a10 10 0 1 0 0 20 10 10 0 0 0 0-20zm6.9 6h-3a15 15 0 0 0-1.3-3.9A8 8 0 0 1 18.9 8zM12 4c.8 1.2 1.5 2.5 1.9 4h-3.8c.4-1.5 1.1-2.8 1.9-4zM4.3 14a8 8 0 0 1 0-4h3.4a16 16 0 0 0 0 4zm.8 2h3a15 15 0 0 0 1.3 3.9A8 8 0 0 1 5.1 16zm3-8h-3a8 8 0 0 1 4.3-3.9A15 15 0 0 0 8.1 8zM12 20c-.8-1.2-1.5-2.5-1.9-4h3.8c-.4 1.5-1.1 2.8-1.9 4zm2.3-6H9.7a14 14 0 0 1 0-4h4.6a14 14 0 0 1 0 4zm.3 5.9a15 15 0 0 0 1.3-3.9h3a8 8 0 0 1-4.3 3.9zm1.7-5.9a16 16 0 0 0 0-4h3.4a8 8 0 0 1 0 4z"/></svg>RinaldoTopPawHaven555.com</li>
    </ul>
  </div>
</section>

</body>
</html>
```